Velvet Shakers business card

We would like a business card designed for our business velvet shakers

We need it to have 2 sides.

More information about the business can be found at www.velvetshakers-example.net

Industry/Entity Type

Business

```html
<!DOCTYPE html>
<html lang="en">
<head>
<meta charset="utf-8">
<title>Velvet Shakers – Business Card</title>
<link href="https://fonts.googleapis.com/css2?family=Lobster&family=Crimson+Text:ital@1&display=swap" rel="stylesheet">
<style>
  :root {
    --backdrop: #d9d7d3;
    --card: #ffffff;
    --card-front: #f1f1f1;
    --gold: #b08a2e;
    --ink: #3a3a3a;
    --shadow: rgba(0, 0, 0, 0.22);
  }
  * { margin: 0; padding: 0; box-sizing: border-box; }
  html, body {
    width: 1200px;
    height: 871px;
    overflow: hidden;
    background: var(--backdrop);
  }
  .canvas {
    position: relative;
    width: 1200px;
    height: 871px;
  }
  .card {
    position: absolute;
    width: 540px;
    height: 310px;
    border-radius: 26px;
    box-shadow: 0 14px 30px var(--shadow);
    overflow: hidden;
  }
  .card--front {
    left: 90px;
    top: 110px;
    background: linear-gradient(160deg, #fafafa 0%, var(--card-front) 55%, #e4e4e4 100%);
  }
  .card--back {
    left: 570px;
    top: 450px;
    background: var(--card);
  }
  .wordmark {
    font-family: "Lobster", cursive;
    color: var(--gold);
    font-weight: 400;
    white-space: nowrap;
  }
  .card--front .wordmark {
    position: absolute;
    left: 0;
    right: 0;
    top: 118px;
    text-align: center;
    font-size: 62px;
  }
  .card--back .wordmark {
    position: absolute;
    right: 40px;
    top: 62px;
    font-size: 40px;
  }
  .holder {
    position: absolute;
    left: 48px;
    top: 78px;
  }
  .holder__name {
    font-family: "Lobster", cursive;
    color: var(--gold);
    font-size: 34px;
    line-height: 1;
  }
  .holder__role {
    font-family: "Crimson Text", serif;
    font-style: italic;
    color: var(--ink);
    font-size: 17px;
    margin-top: 6px;
  }
  .contact {
    position: absolute;
    left: 48px;
    top: 170px;
    list-style: none;
  }
  .contact__item {
    display: flex;
    align-items: center;
    gap: 14px;
    font-family: "Crimson Text", serif;
    font-style: italic;
    color: var(--ink);
    font-size: 17px;
    height: 30px;
  }
  .contact__icon {
    width: 16px;
    height: 16px;
    flex: none;
  }
</style>
</head>
<body>
<main class="canvas">

  <section class="card card--front" aria-label="Card front">
    <div class="wordmark">Velvet Shakers</div>
  </section>

  <section class="card card--back" aria-label="Card back">
    <div class="holder">
      <div class="holder__name">Marco Reyes</div>
      <div class="holder__role">Founder</div>
    </div>

    <div class="wordmark">Velvet Shakers</div>

    <ul class="contact">
      <li class="contact__item">
        <svg class="contact__icon" viewBox="0 0 16 16" aria-hidden="true">
          <rect x="0" y="0" width="16" height="16" rx="3" fill="var(--gold)"/>
          <path d="M5 4 L7 6 L6 7.5 Q7.5 9.5 8.5 10 L10 9 L12 11 L10.5 12.3 Q6 11.5 3.8 5.5 Z" fill="#fff"/>
        </svg>
        0400 555 101
      </li>
      <li class="contact__item">
        <svg class="contact__icon" viewBox="0 0 16 16" aria-hidden="true">
          <rect x="0" y="0" width="16" height="16" rx="3" fill="var(--gold)"/>
          <path d="M5 4 L7 6 L6 7.5 Q7.5 9.5 8.5 10 L10 9 L12 11 L10.5 12.3 Q6 11.5 3.8 5.5 Z" fill="#fff"/>
        </svg>
        0400 555 202
      </li>
      <li class="contact__item">
        <svg class="contact__icon" viewBox="0 0 16 16" aria-hidden="true">
          <rect x="0" y="0" width="16" height="16" rx="3" fill="var(--gold)"/>
          <rect x="3.5" y="5" width="9" height="6.5" fill="#fff"/>
          <path d="M3.5 5 L8 8.6 L12.5 5" fill="none" stroke="var(--gold)" stroke-width="1"/>
        </svg>
        info@velvetshakers-example.net
      </li>
    </ul>
  </section>

</main>
</body>
</html>
```